Разработка этикеток для моющих средств
Задание на дизайн
Размер
160 мм × 160 мм
Опишите свою организацию или продукт и целевую аудиторию
Мы выпускаем моющие средства нового поколения.
Основная линейка продуктов:
- автошампуни для автомоек
- автошампуни для ручной мойки
- незамерзающая жидкость (стеклоомывайка)
- клиниг
Целевые аудитории:
- обычные автовладельцы
- автомойки
- клининговые компании.
Цвета:
- для каждого направления необходимо подобрать свой цвет этикетки (или вставки различных цветов) Цвета должны быть привлекательными, насыщенными, строгими.
Какой должна быть этикетка:
-выделяющаяся на полках магазина (возможно строгостью)
-должна вызывать желание брать и использовать. (возможно премиальность)
-размер этикетки 160*160 мм., но нужен будет еще и более узкий вариант, для маленького объема размером 134*76 мм. (высота*ширина)
Пожелания:
-Этикетка не должна быть перегружена.
-Текст должен быть понятен.
-Логотип должен быть заметным (возможно разместить сверку или в углу сверху)
-Цвет и фон можно менять.
-Этикетка будет односторонней (текст для этикетки, а именно состав, штрих код и пр. будет предоставлена победителю для размещения).
-Обязательно оставляем место для штрих-кода, описания, состава, пропорциях разбавления, предупреждения (к стеклоомывайке разбавление не относится)
Ждем интересных проектов.
Банальные и нелепые этикетки просим не высылать!!!
Дополнительно:
-Прошу Вас не размещать изображение автомобилей, транспорта на этикетку
-Логотип не обязательно размещать на всю ширину или высоту этикетки (можно ограничится горизонтальной вставкой слева сверху)
-В написании продукции используйте названия к продукции, например: Zelto, Ferin, Tirel
Ниже представлены понравившиеся варианты, но это не значит, что должно быть именно так, должен быть свой уникальный дизайн, мы не повторяем других и не стараемся быть как они.
привлекает дизайн этикетки.
расположение информации будет примерно такое же.
данные канистры будут использоваться

```html
<!DOCTYPE html>
<html lang="ru">
<head>
<meta charset="utf-8">
<title>VELTRAN — этикетки линейки</title>
<link rel="stylesheet" href="https://fonts.googleapis.com/css2?family=Roboto+Condensed:wght@400;700;900&display=swap">
<style>
  :root{
    --wash:#a9c990;
    --hand:#ecc92b;
    --frost:#c6e0f3;
    --clean:#b4d5cd;
    --ink:#111111;
    --paper:#ffffff;
    --frame:#d9d9d9;
    --font:"Roboto Condensed", "Arial Narrow", sans-serif;
  }
  *{box-sizing:border-box;margin:0;padding:0}
  html,body{width:1200px;height:830px;overflow:hidden;background:var(--paper)}
  body{position:relative;font-family:var(--font);color:var(--ink)}

  .label{position:absolute;width:382px;height:381px;background:var(--paper)}
  .label--wash{--tone:var(--wash)}
  .label--hand{--tone:var(--hand)}
  .label--frost{--tone:var(--frost)}
  .label--clean{--tone:var(--clean)}

  .label__head{position:absolute;left:0;top:0;width:382px;height:118px;background:var(--tone)}
  .label__line{position:absolute;left:15px;top:10px;font-weight:700;font-size:17px;letter-spacing:.3px}
  .label__brand{position:absolute;left:13px;top:25px;font-weight:900;font-size:54px;line-height:1;letter-spacing:.5px}
  .label__type{position:absolute;left:15px;top:84px;font-weight:700;font-size:15.5px;text-transform:uppercase}
  .label__figure{position:absolute;left:272px;top:26px;width:96px;height:92px;
    background:linear-gradient(160deg,rgba(17,17,17,.15),rgba(17,17,17,.85));border-radius:40px 40px 0 0}
  .label__bar{position:absolute;left:0;top:118px;width:382px;height:13px;background:var(--ink)}

  .label__icons{position:absolute;left:15px;top:154px;width:100px;display:grid;grid-template-columns:50px 50px;row-gap:14px}
  .icon{display:flex;flex-direction:column;align-items:center;width:44px}
  .icon svg{width:31px;height:31px}
  .icon span{font-size:5.5px;font-weight:700;margin-top:3px}

  .label__info{position:absolute;left:128px;top:155px;width:245px;font-size:7px;line-height:11.8px;text-transform:uppercase;font-weight:400}
  .label__info p{margin-bottom:6px}
  .label__info b{font-weight:700}

  .label__decor{position:absolute;left:280px;top:268px;width:100px;height:82px;
    background:radial-gradient(ellipse at 60% 50%,rgba(150,195,230,.55),rgba(198,224,243,0) 70%)}

  .label__warn{position:absolute;left:0;top:352px;width:382px;height:29px;background:var(--tone);
    padding:2px 15px 0;font-weight:700;font-size:11px;line-height:12px;text-transform:uppercase;letter-spacing:.3px}

  .slim{position:absolute;left:406px;top:411px;width:182px;height:320px;background:var(--paper)}
  .slim__strip{position:absolute;left:0;top:0;width:53px;height:320px;background:var(--wash)}
  .slim__figure{position:absolute;left:10px;top:10px;width:36px;height:46px;border-radius:14px 14px 0 0;
    background:linear-gradient(160deg,rgba(17,17,17,.15),rgba(17,17,17,.85))}
  .slim__brand{position:absolute;left:27px;top:315px;transform-origin:0 0;transform:rotate(-90deg) translateY(-50%);
    font-weight:900;font-size:46px;line-height:1;white-space:nowrap}
  .slim__rule{position:absolute;left:53px;top:0;width:7px;height:320px;background:var(--ink)}
  .slim__edge{position:absolute;right:0;top:0;width:6px;height:320px;background:var(--wash)}
  .slim__line{position:absolute;left:66px;top:8px;font-weight:700;font-size:17px}
  .slim__type{position:absolute;left:66px;top:33px;font-weight:700;font-size:7.5px;text-transform:uppercase}
  .slim__info{position:absolute;left:66px;top:47px;width:110px;font-size:6.2px;line-height:11.8px;text-transform:uppercase}
  .slim__info p{margin-bottom:4px}
  .slim__info b{font-weight:700}
  .slim__icons{position:absolute;left:72px;top:226px;width:100px;display:grid;grid-template-columns:60px 40px;row-gap:6px}
  .slim__icons .icon svg{width:25px;height:25px}

  .mockup{position:absolute;background:var(--paper);border:1px solid var(--frame)}
  .mockup--bottle{left:597px;top:411px;width:310px;height:320px}
  .mockup--can{left:883px;top:419px;width:310px;height:312px}
  .mockup__scene{position:absolute;inset:14px 70px;border-radius:18px;
    background:linear-gradient(180deg,#e9ecef 0%,#f6f7f8 40%,#dfe3e6 100%)}
  .mockup--can .mockup__scene{inset:30px 40px 40px}
</style>
</head>
<body>

<svg width="0" height="0" style="position:absolute" aria-hidden="true">
  <defs>
    <symbol id="ico-tap" viewBox="0 0 40 40"><circle cx="20" cy="20" r="18.5" fill="none" stroke="#111" stroke-width="2"/><path d="M10 15h14v5h-4v3h-4v-3h-6z" fill="#111"/><path d="M16 11h6" stroke="#111" stroke-width="2"/><path d="M18 27c0 2 1 3 1 3s1-1 1-3-1-2-1-2-1 0-1 2z" fill="#111"/></symbol>
    <symbol id="ico-clock" viewBox="0 0 40 40"><circle cx="20" cy="20" r="18.5" fill="none" stroke="#111" stroke-width="2"/><circle cx="20" cy="20" r="11" fill="none" stroke="#111" stroke-width="2"/><path d="M20 13v7l5 3" fill="none" stroke="#111" stroke-width="2"/></symbol>
    <symbol id="ico-spray" viewBox="0 0 40 40"><circle cx="20" cy="20" r="18.5" fill="none" stroke="#111" stroke-width="2"/><rect x="15" y="15" width="10" height="17" rx="3" fill="none" stroke="#111" stroke-width="2"/><path d="M17 15v-4h8l3 2" fill="none" stroke="#111" stroke-width="2"/></symbol>
    <symbol id="ico-sprayer" viewBox="0 0 40 40"><circle cx="20" cy="20" r="18.5" fill="none" stroke="#111" stroke-width="2"/><rect x="14" y="14" width="12" height="18" rx="5" fill="none" stroke="#111" stroke-width="2"/><path d="M20 14v-4M26 18l6-6M9 31l22-22" fill="none" stroke="#111" stroke-width="2"/></symbol>
  </defs>
</svg>

<!-- Tirel — car wash shampoo -->
<article class="label label--wash" style="left:13px;top:17px">
  <header class="label__head">
    <span class="label__line">TIREL</span>
    <span class="label__brand">VELTRAN</span>
    <span class="label__type">Автошампунь для автомоек</span>
    <div class="label__figure" role="img" aria-label="Силуэт человека, сидящего на стуле с журналом"></div>
  </header>
  <div class="label__bar"></div>
  <div class="label__icons">
    <div class="icon"><svg><use href="#ico-tap"/></svg><span>НАДПИСЬ</span></div>
    <div class="icon"><svg><use href="#ico-clock"/></svg><span>НАДПИСЬ</span></div>
    <div class="icon"><svg><use href="#ico-spray"/></svg><span>НАДПИСЬ</span></div>
    <div class="icon"><svg><use href="#ico-sprayer"/></svg><span>НАДПИСЬ</span></div>
  </div>
  <div class="label__info">
    <p><b>Описание:</b> текст текст текст текст текст екст текст текст текст текст тексттекст текст текст текст текст текст екст текст текст текст текст тексттекст текст текст текст текст текст екст текст текст текст тексттекст текст текст текст текст тексттекст текст текст текст текст</p>
    <p><b>Состав:</b> текст текст текст текст текст текст текст текст текст текст текст тексттексттекст текст текст текст текст текст текст текст текст текст текст текст</p>
    <p><b>Пропорции разбавления:</b> текст текст текст текст текст текст текст текст текст текст текст текст текст текст текст текст текст текст текст текст текст текст текст т</p>
    <p><b>Меры предосторожности:</b> текст текст текст текст текст текст текст текст</p>
  </div>
  <p class="label__warn">Предупреждение: текст текст текст текст текст текст текст<br>текст ттекст текст текст текст текст текст текст текст текст</p>
</article>

<!-- Tirel — hand wash shampoo -->
<article class="label label--hand" style="left:406px;top:17px">
  <header class="label__head">
    <span class="label__line">TIREL</span>
    <span class="label__brand">VELTRAN</span>
    <span class="label__type">Автошампунь для ручной мойки</span>
    <div class="label__figure" role="img" aria-label="Силуэт человека, сидящего на стуле с журналом"></div>
  </header>
  <div class="label__bar"></div>
  <div class="label__icons">
    <div class="icon"><svg><use href="#ico-tap"/></svg><span>НАДПИСЬ</span></div>
    <div class="icon"><svg><use href="#ico-clock"/></svg><span>НАДПИСЬ</span></div>
    <div class="icon"><svg><use href="#ico-spray"/></svg><span>НАДПИСЬ</span></div>
    <div class="icon"><svg><use href="#ico-sprayer"/></svg><span>НАДПИСЬ</span></div>
  </div>
  <div class="label__info">
    <p><b>Описание:</b> текст текст текст текст текст екст текст текст текст текст тексттекст текст текст текст текст текст екст текст текст текст текст тексттекст текст текст текст текст текст екст текст текст текст тексттекст текст текст текст текст тексттекст текст текст текст текст</p>
    <p><b>Состав:</b> текст текст текст текст текст текст текст текст текст текст текст тексттексттекст текст текст текст текст текст текст текст текст текст текст текст</p>
    <p><b>Пропорции разбавления:</b> текст текст текст текст текст текст текст текст текст текст текст текст текст текст текст текст текст текст текст текст текст текст текст т</p>
    <p><b>Меры предосторожности:</b> текст текст текст текст текст текст текст текст</p>
  </div>
  <p class="label__warn">Предупреждение: текст текст текст текст текст текст текст<br>текст ттекст текст текст текст текст текст текст текст текст</p>
</article>

<!-- Ferin — screen wash -->
<article class="label label--frost" style="left:801px;top:17px">
  <header class="label__head">
    <span class="label__line">FERIN</span>
    <span class="label__brand">VELTRAN</span>
    <span class="label__type">Незамерзающая жидкость</span>
    <div class="label__figure" role="img" aria-label="Силуэт человека в шапке, сидящего на стуле с журналом"></div>
  </header>
  <div class="label__bar"></div>
  <div class="label__icons">
    <div class="icon"><svg><use href="#ico-tap"/></svg><span>НАДПИСЬ</span></div>
    <div class="icon"><svg><use href="#ico-clock"/></svg><span>НАДПИСЬ</span></div>
    <div class="icon"><svg><use href="#ico-spray"/></svg><span>НАДПИСЬ</span></div>
    <div class="icon"><svg><use href="#ico-sprayer"/></svg><span>НАДПИСЬ</span></div>
  </div>
  <div class="label__info" style="top:163px">
    <p><b>Описание:</b> текст текст текст текст текст екст текст текст текст текст тексттекст текст текст текст текст текст екст текст текст текст текст тексттекст текст текст текст текст текст екст текст текст текст тексттекст текст текст текст текст тексттекст текст текст текст текст</p>
    <p><b>Состав:</b> текст текст текст текст текст текст текст текст текст текст текст тексттексттекст текст текст текст текст текст текст текст текст текст текст текст</p>
    <p><b>Меры предосторожности:</b> текст текст текст<br>текст текст текст текст текст текст</p>
  </div>
  <div class="label__decor" role="img" aria-label="Россыпь снежинок"></div>
  <p class="label__warn">Предупреждение: текст текст текст текст текст текст текст<br>текст ттекст текст текст текст текст текст текст текст текст</p>
</article>

<!-- Zelto — cleaning -->
<article class="label label--clean" style="left:13px;top:411px">
  <header class="label__head">
    <span class="label__line">ZELTO</span>
    <span class="label__brand">VELTRAN</span>
    <span class="label__type" style="top:87px">Клининг</span>
    <div class="label__figure" role="img" aria-label="Силуэт человека, сидящего на стуле с журналом"></div>
  </header>
  <div class="label__bar"></div>
  <div class="label__icons">
    <div class="icon"><svg><use href="#ico-tap"/></svg><span>НАДПИСЬ</span></div>
    <div class="icon"><svg><use href="#ico-clock"/></svg><span>НАДПИСЬ</span></div>
    <div class="icon"><svg><use href="#ico-spray"/></svg><span>НАДПИСЬ</span></div>
    <div class="icon"><svg><use href="#ico-sprayer"/></svg><span>НАДПИСЬ</span></div>
  </div>
  <div class="label__info">
    <p><b>Описание:</b> текст текст текст текст текст екст текст текст текст текст тексттекст текст текст текст текст текст екст текст текст текст текст тексттекст текст текст текст текст текст екст текст текст текст тексттекст текст текст текст текст тексттекст текст текст текст текст</p>
    <p><b>Состав:</b> текст текст текст текст текст текст текст текст текст текст текст тексттексттекст текст текст текст текст текст текст текст текст текст текст текст</p>
    <p><b>Пропорции разбавления:</b> текст текст текст текст текст текст текст текст текст текст текст текст текст текст текст текст текст текст текст текст текст текст текст т</p>
    <p><b>Меры предосторожности:</b> текст текст текст текст текст текст текст текст</p>
  </div>
  <p class="label__warn">Предупреждение: текст текст текст текст текст текст текст<br>текст ттекст текст текст текст текст текст текст текст текст</p>
</article>

<!-- Tirel — narrow label for small volume -->
<article class="slim">
  <div class="slim__strip"></div>
  <div class="slim__figure" role="img" aria-label="Силуэт человека, сидящего на стуле с журналом"></div>
  <span class="slim__brand">VELTRAN</span>
  <div class="slim__rule"></div>
  <div class="slim__edge"></div>
  <span class="slim__line">TIREL</span>
  <span class="slim__type">Автошампунь для автомоек</span>
  <div class="slim__info">
    <p><b>Описание:</b> текст текст текст текст екст текст текст текст текст тексттекст текст текст текст текст текст екст текст текст текст</p>
    <p><b>Состав:</b> текст текст текст текст текст текст текст текст текст тексттексттекст</p>
    <p><b>Пропорции разбавления:</b> текст текст текст текст текст</p>
    <p><b>Меры предосторожности:</b> текст текст текст текст текст текст текст текст</p>
  </div>
  <div class="slim__icons">
    <div class="icon"><svg><use href="#ico-tap"/></svg><span>НАДПИСЬ</span></div>
    <div class="icon"><svg><use href="#ico-clock"/></svg><span>НАДПИСЬ</span></div>
    <div class="icon"><svg><use href="#ico-spray"/></svg><span>НАДПИСЬ</span></div>
  </div>
</article>

<!-- Packaging previews -->
<figure class="mockup mockup--bottle">
  <div class="mockup__scene" role="img" aria-label="Белая бутылка с красной крышкой и узкой зелёной этикеткой Tirel"></div>
</figure>
<figure class="mockup mockup--can">
  <div class="mockup__scene" role="img" aria-label="Полупрозрачная канистра с красной крышкой и зелёной этикеткой Tirel"></div>
</figure>

</body>
</html>
```